Professional Simple Business Card Design

Design a professional business card . Simple Design.
Base colour White and purple(logo colour) which is from the logo attached. Other logo colour(orange) can be used if required.
Include dummy name and designation column which can be filled for later purpose.

Find attached Logo and other details.

```html
<!DOCTYPE html>
<html lang="en">
<head>
<meta charset="utf-8">
<title>Orvane Formulations – Business Card</title>
<link rel="stylesheet" href="https://fonts.googleapis.com/css2?family=Lato:wght@400;700&display=swap">
<style>
  :root {
    --purple: #7a4fa3;
    --orange: #f28a2a;
    --white: #ffffff;
    --backdrop: #2c2e33;
  }
  * { margin: 0; padding: 0; box-sizing: border-box; }
  html, body {
    width: 1200px; height: 900px; overflow: hidden;
    background: var(--backdrop);
    font-family: "Lato", Arial, sans-serif;
  }
  .sheet {
    position: relative; width: 1200px; height: 900px;
    display: flex; flex-direction: column; align-items: center; justify-content: center; gap: 40px;
  }
  .card {
    position: relative; width: 660px; height: 377px;
    background: var(--white); overflow: hidden;
    box-shadow: 0 10px 30px rgba(0,0,0,0.35);
  }
  .card-shapes { position: absolute; inset: 0; width: 100%; height: 100%; }
  .brand {
    position: absolute; display: flex; align-items: center; gap: 12px;
  }
  .brand-dot {
    width: 22px; height: 22px; border-radius: 50%; background: var(--orange); flex: none;
  }
  .brand-name {
    color: var(--purple); font-weight: 700; font-size: 30px; line-height: 1.08;
    letter-spacing: 1px; text-transform: uppercase; white-space: nowrap;
  }
  .card-front .brand { left: 290px; top: 112px; }
  .card-back .brand { left: 340px; top: 130px; }
  .website {
    position: absolute; left: 70px; bottom: 30px;
    color: var(--orange); font-size: 14px; letter-spacing: 0.3px;
  }
  .contact-list {
    position: absolute; left: 40px; top: 34px; list-style: none;
    display: flex; flex-direction: column; gap: 10px;
  }
  .contact-item {
    display: flex; align-items: flex-start; gap: 10px;
    color: var(--orange); font-size: 12.5px; line-height: 1.35; white-space: nowrap;
  }
  .contact-icon {
    width: 18px; height: 18px; flex: none; background: var(--white);
    display: flex; align-items: center; justify-content: center; margin-top: 1px;
  }
  .contact-icon svg { width: 12px; height: 12px; }
  .holder {
    position: absolute; left: 40px; top: 314px; color: var(--white);
  }
  .holder-name { font-size: 17px; font-weight: 700; letter-spacing: 0.5px; }
  .holder-role { font-size: 12.5px; color: var(--orange); margin-top: 3px; }
</style>
</head>
<body>
<main class="sheet">

  <section class="card card-front" aria-label="Card front">
    <svg class="card-shapes" viewBox="0 0 660 377" aria-hidden="true">
      <rect x="0" y="297" width="660" height="80" fill="var(--purple)"/>
    </svg>
    <div class="brand">
      <span class="brand-dot"></span>
      <span class="brand-name">Orvane<br>Formulations</span>
    </div>
    <p class="website">www.orvaneformulations.com</p>
  </section>

  <section class="card card-back" aria-label="Card back">
    <svg class="card-shapes" viewBox="0 0 660 377" aria-hidden="true">
      <rect x="0" y="0" width="660" height="377" fill="var(--purple)"/>
      <polygon points="230,0 660,0 660,300 150,300 310,165" fill="var(--white)"/>
    </svg>
    <ul class="contact-list">
      <li class="contact-item">
        <span class="contact-icon">
          <svg viewBox="0 0 24 24"><path fill="var(--purple)" d="M6.6 10.8a15.1 15.1 0 0 0 6.6 6.6l2.2-2.2c.3-.3.7-.4 1-.2 1.1.4 2.3.6 3.6.6.6 0 1 .4 1 1V20c0 .6-.4 1-1 1A17 17 0 0 1 3 4c0-.6.4-1 1-1h3.5c.6 0 1 .4 1 1 0 1.3.2 2.5.6 3.6.1.3 0 .7-.2 1l-2.3 2.2z"/></svg>
        </span>
        <span>044-31597260</span>
      </li>
      <li class="contact-item">
        <span class="contact-icon">
          <svg viewBox="0 0 24 24"><path fill="var(--purple)" d="M12 2a7 7 0 0 0-7 7c0 5.2 7 13 7 13s7-7.8 7-13a7 7 0 0 0-7-7zm0 9.5a2.5 2.5 0 1 1 0-5 2.5 2.5 0 0 1 0 5z"/></svg>
        </span>
        <span>No.14, Cedar Court, 2nd Floor,<br>Riverside Industrial Estate,<br>Maple Nagar, Westfield,<br>Northbay 600482</span>
      </li>
      <li class="contact-item">
        <span class="contact-icon">
          <svg viewBox="0 0 24 24"><path fill="var(--purple)" d="M2 5h20v14H2V5zm2 2v.5l8 5 8-5V7H4z"/></svg>
        </span>
        <span>contact@orvaneformulations.com</span>
      </li>
    </ul>
    <div class="brand">
      <span class="brand-dot"></span>
      <span class="brand-name">Orvane<br>Formulations</span>
    </div>
    <div class="holder">
      <p class="holder-name">Your Name</p>
      <p class="holder-role">Designation</p>
    </div>
  </section>

</main>
</body>
</html>
```